Business Card Design Project

I need a new business card for side business. Very simple and to the point. I am a licensed massage therapist and want the colors to be warm. I don't have a logo or company name. I just need to convey that I am a Licensed Massage Therapist and have my contact information so people can contact me. I'll attach some files that I like. I am a male so I don't want it to be feminine.

One file is my existing card. I like Tessa's card and the layout so would prefer a similar layout. I would like to incorporate my swimmer/biker/runner image. Doesn't have to be the exact likeness because I don't have that file but something similar to that. I would like to also include my areas of specialty of: Swedish, Deep Tissue, Sports, and Hot Stone

I would also like to incorporate a QR code on the back of the card centered.
Updates

Payment is NOW guaranteed to the design I choose.  I updated my creative brief so hopefully it is more clear.  

Industry/Entity Type

Massage

Requirements
Must have
• Glen Harwick
Licensed Massage Therapist
or
Massage Therapy
203-555-0147
gharwick@mailbrook.example

```html
<!DOCTYPE html>
<html lang="en">
<head>
<meta charset="UTF-8">
<title>Glen Harwick – Licensed Massage Therapist</title>
<link rel="stylesheet" href="https://fonts.googleapis.com/css2?family=PT+Sans:wght@400&display=swap">
<style>
  :root {
    --card-bg: #f5ece3;
    --card-edge: #d3d1cf;
    --name-brown: #8a5a32;
    --title-tan: #a57c55;
    --contact-brown: #7f5531;
    --rule-brown: #6b3f1f;
    --art-light: #d9b48c;
    --art-dark: #a97a4c;
  }
  * { margin: 0; padding: 0; box-sizing: border-box; }
  html, body {
    width: 1200px;
    height: 698px;
    overflow: hidden;
    background: var(--card-bg);
  }
  .business-card {
    position: relative;
    width: 1200px;
    height: 698px;
    background: var(--card-bg);
    border: 4px solid var(--card-edge);
    font-family: "PT Sans", "Myriad Pro", sans-serif;
  }
  .therapist-name {
    position: absolute;
    left: 71px;
    top: 100px;
    font-size: 54px;
    font-weight: 400;
    color: var(--name-brown);
    letter-spacing: -0.5px;
  }
  .therapist-title {
    position: absolute;
    left: 71px;
    top: 199px;
    font-size: 38px;
    font-weight: 400;
    color: var(--title-tan);
  }
  .contact-list {
    position: absolute;
    left: 75px;
    top: 352px;
    list-style: none;
    font-size: 27px;
    color: var(--contact-brown);
  }
  .contact-list li { height: 59px; }
  .contact-list .contact-email { margin-left: -3px; }
  .athlete-artwork {
    position: absolute;
    left: 926px;
    top: 84px;
    width: 190px;
    height: 398px;
    border-radius: 95px 40px 40px 95px;
    background: linear-gradient(160deg, var(--art-light), var(--art-dark));
    opacity: 0.55;
  }
  .divider-rule {
    position: absolute;
    left: 231px;
    top: 528px;
    width: 710px;
    height: 4px;
    border-radius: 2px;
    background: var(--rule-brown);
  }
  .specialty-list {
    position: absolute;
    left: 160px;
    top: 571px;
    width: 878px;
    display: flex;
    justify-content: space-between;
    list-style: none;
    font-size: 36px;
    color: var(--contact-brown);
  }
  .specialty-list .separator { font-weight: 400; }
</style>
</head>
<body>
  <main class="business-card">
    <h1 class="therapist-name">Glen Harwick</h1>
    <p class="therapist-title">Licensed Massage Therapist</p>

    <ul class="contact-list">
      <li class="contact-phone">203-555-0147</li>
      <li class="contact-email">gharwick@mailbrook.example</li>
    </ul>

    <div class="athlete-artwork" role="img" aria-label="Illustration of a swimmer, a cyclist and a runner beside a curved trail of dots, in warm tan tones"></div>

    <div class="divider-rule"></div>

    <ul class="specialty-list">
      <li>Swedish</li>
      <li class="separator" aria-hidden="true">|</li>
      <li>Deep Tissue</li>
      <li class="separator" aria-hidden="true">|</li>
      <li>Sports</li>
      <li class="separator" aria-hidden="true">|</li>
      <li>Hot Stone</li>
    </ul>
  </main>
</body>
</html>
```